Yard Signs - Fiber Optic Customer

I need an awesome design for a yard sign for our new customers.  We are installing a fiber optic network and are going to give new customers the option to put a yard sign up in exchange for a free month of service.  I want to use printholm-example.com.  A blank template is available there for the large (27x18) yard signs.
Requirements:
-our website is (needs to be on sign):  www.brindlelinknet.example
-our phone:  402-555-0148
-our logo
-a graphic that conveys 'connected'
I want it to say something to the effect.. I'm connected to Brindle Fiber.  The fastest high-speed internet available.  Crystal clear telephone.  I don't necessarily need that specific wording, something along those lines.
Contact me with questions:  owen@brindlelinknet.example

Industry/Entity Type
Internet

```html
<!DOCTYPE html>
<html lang="en">
<head>
<meta charset="utf-8">
<title>Brindle Fiber Yard Sign</title>
<link rel="stylesheet" href="https://fonts.googleapis.com/css2?family=Jost:wght@400;600&display=swap">
<style>
  :root {
    --page-bg: #e9ecef;
    --frame: #9a9ea3;
    --frame-light: #c4c7cb;
    --panel-white: #ffffff;
    --brand-blue: #1f6fa6;
    --blue-deep: #0f4f86;
    --blue-mid: #2a74b4;
    --blue-light: #7fb2dc;
    --fiber-glow: #d6e8f6;
    --text-light: #ffffff;
  }
  * { box-sizing: border-box; margin: 0; padding: 0; }
  html, body {
    width: 1200px;
    height: 652px;
    overflow: hidden;
    background: var(--page-bg);
    font-family: "Jost", "Futura", sans-serif;
  }
  .canvas {
    position: relative;
    width: 1200px;
    height: 652px;
  }
  .yard-sign {
    position: absolute;
    left: 147px;
    top: 20px;
    width: 906px;
    height: 612px;
    padding: 14px;
    background: linear-gradient(180deg, var(--frame-light), var(--frame));
    border-radius: 3px;
  }
  .sign-face {
    width: 100%;
    height: 100%;
    display: flex;
    flex-direction: column;
  }
  .brand-band {
    height: 216px;
    background: var(--panel-white);
    display: flex;
    align-items: center;
    justify-content: center;
  }
  .brand-name {
    font-weight: 600;
    font-size: 96px;
    letter-spacing: 1px;
    color: var(--brand-blue);
    line-height: 1;
  }
  .message-band {
    position: relative;
    flex: 1;
    overflow: hidden;
  }
  .fiber-photo {
    position: absolute;
    inset: 0;
    background:
      radial-gradient(ellipse 38% 60% at 68% 70%, var(--fiber-glow) 0%, rgba(170,205,235,0.45) 35%, transparent 75%),
      linear-gradient(100deg, var(--blue-light) 0%, var(--blue-mid) 35%, var(--blue-deep) 100%);
  }
  .message-list {
    position: relative;
    list-style: none;
    text-align: center;
    color: var(--text-light);
    font-size: 37px;
    font-weight: 400;
    padding-top: 38px;
  }
  .message-list li {
    line-height: 72px;
    display: flex;
    justify-content: center;
    align-items: center;
    gap: 12px;
  }
  .bullet {
    width: 10px;
    height: 10px;
    border-radius: 50%;
    background: var(--text-light);
  }
  .contact-line {
    position: absolute;
    left: 0;
    right: 0;
    bottom: 26px;
    display: flex;
    justify-content: center;
    align-items: center;
    gap: 18px;
    color: var(--text-light);
    font-size: 33px;
  }
  .contact-item { display: flex; align-items: center; gap: 10px; }
  .contact-icon { width: 28px; height: 28px; }
</style>
</head>
<body>
<div class="canvas">
  <div class="yard-sign">
    <div class="sign-face">
      <div class="brand-band">
        <span class="brand-name">BRINDLE</span>
      </div>
      <div class="message-band">
        <div class="fiber-photo" role="img" aria-label="Photograph of two fiber optic cable connectors crossing, their glowing strand ends conveying a live connection, in blue tones"></div>
        <ul class="message-list">
          <li><span class="bullet"></span>I'm connected to Brindle Fiber!</li>
          <li><span class="bullet"></span>The fastest high-speed internet available.</li>
          <li><span class="bullet"></span>Crystal clear telephone.</li>
        </ul>
        <div class="contact-line">
          <span class="contact-item">
            <svg class="contact-icon" viewBox="0 0 28 28" aria-hidden="true">
              <circle cx="14" cy="14" r="12" fill="none" stroke="#fff" stroke-width="2"/>
              <path d="M9 7.5 h3.5 l1 4 l-2 1.6 q1.6 3 4.4 4.4 l1.6 -2 l4 1 v3.5 h-1 q-11 -0.5 -11.5 -12.5z" fill="#fff"/>
            </svg>
            402-555-0148
          </span>
          <span class="contact-item">
            <svg class="contact-icon" viewBox="0 0 28 28" aria-hidden="true">
              <g fill="none" stroke="#fff" stroke-width="1.8">
                <circle cx="14" cy="14" r="11"/>
                <ellipse cx="14" cy="14" rx="5" ry="11"/>
                <line x1="3" y1="14" x2="25" y2="14"/>
                <line x1="5" y1="8.5" x2="23" y2="8.5"/>
                <line x1="5" y1="19.5" x2="23" y2="19.5"/>
              </g>
            </svg>
            www.brindlelinknet.example
          </span>
        </div>
      </div>
    </div>
  </div>
</div>
</body>
</html>
```